Dyrano In-home Personal Training

I would like to have some eye-catching business card design. Opened to any ideas.

The business idea: mobile fitness - train clients at their places

Target Market(s)

General population, 20-60 years old

Industry/Entity Type

Fitness

Contact Information for Business Card

The information to include:
Name: Marta
Call or text: 306-555-0187
Website: Dyrano.ca
Please use the attached logo

Requirements
Should not have
• No orange or purple colours please

```html
<!DOCTYPE html>
<html lang="en">
<head>
<meta charset="utf-8">
<title>Dyrano In-home Personal Training – Business Card</title>
<link rel="stylesheet" href="https://fonts.googleapis.com/css2?family=Raleway:wght@200&family=Oswald:wght@500&family=Open+Sans:wght@400&display=swap">
<style>
  :root {
    --page-bg: #e9e7e3;
    --card-blue: #1f9ad6;
    --card-blue-deep: #1679b8;
    --frost-light: #e4e1dc;
    --frost-mid: #cfcbc4;
    --ink-light: #efe8dc;
    --ink-soft: #e2dbcf;
  }
  * { box-sizing: border-box; margin: 0; padding: 0; }
  html, body {
    width: 1200px;
    height: 970px;
    overflow: hidden;
    background: var(--page-bg);
  }
  .canvas {
    position: relative;
    width: 1200px;
    height: 970px;
  }
  .card {
    position: absolute;
    left: 80px;
    top: 196px;
    width: 1040px;
    height: 578px;
    overflow: hidden;
    background: linear-gradient(160deg, var(--frost-light) 0%, var(--frost-mid) 100%);
    box-shadow: 0 10px 30px rgba(0, 0, 0, 0.18);
  }
  .card__blue-field {
    position: absolute;
    inset: 0;
    background:
      linear-gradient(118deg,
        var(--card-blue) 0%,
        var(--card-blue) 38%,
        rgba(31, 154, 214, 0.75) 52%,
        rgba(31, 154, 214, 0) 64%);
  }
  .card__blue-field::after {
    content: "";
    position: absolute;
    inset: 0;
    background: linear-gradient(180deg, rgba(22, 121, 184, 0) 40%, rgba(22, 121, 184, 0.35) 100%);
    mask-image: linear-gradient(90deg, #000 0%, #000 40%, transparent 60%);
    -webkit-mask-image: linear-gradient(90deg, #000 0%, #000 40%, transparent 60%);
  }
  .brand {
    position: absolute;
    left: 38px;
    top: 30px;
  }
  .brand__name {
    font-family: "Raleway", sans-serif;
    font-weight: 200;
    font-size: 100px;
    line-height: 1;
    letter-spacing: 20px;
    color: var(--ink-light);
  }
  .brand__tagline {
    margin-top: 14px;
    font-family: "Open Sans", sans-serif;
    font-weight: 400;
    font-size: 19px;
    letter-spacing: 3.6px;
    color: var(--ink-light);
  }
  .contact {
    position: absolute;
    left: 40px;
    top: 378px;
  }
  .contact__name {
    font-family: "Oswald", sans-serif;
    font-weight: 500;
    font-size: 44px;
    line-height: 1.1;
    letter-spacing: 0.5px;
    color: var(--ink-light);
    margin-bottom: 18px;
  }
  .contact__list { list-style: none; }
  .contact__item {
    display: flex;
    align-items: center;
    gap: 14px;
    height: 39px;
    font-family: "Open Sans", sans-serif;
    font-size: 22px;
    color: var(--ink-soft);
  }
  .contact__icon {
    width: 22px;
    height: 22px;
    fill: var(--ink-soft);
    flex: none;
  }
</style>
</head>
<body>
<div class="canvas">
  <section class="card" aria-label="Dyrano business card">
    <div class="card__blue-field"></div>

    <header class="brand">
      <h1 class="brand__name">Dyrano</h1>
      <p class="brand__tagline">IN - HOME PERSONAL TRAINING</p>
    </header>

    <div class="contact">
      <h2 class="contact__name">MARTA KOVRINA</h2>
      <ul class="contact__list">
        <li class="contact__item">
          <svg class="contact__icon" viewBox="0 0 24 24" aria-hidden="true"><path d="M6.6 10.8c1.4 2.8 3.8 5.1 6.6 6.6l2.2-2.2c.3-.3.7-.4 1-.2 1.1.4 2.3.6 3.6.6.6 0 1 .4 1 1V20c0 .6-.4 1-1 1C10.6 21 3 13.4 3 4c0-.6.4-1 1-1h3.5c.6 0 1 .4 1 1 0 1.3.2 2.5.6 3.6.1.3 0 .7-.2 1l-2.3 2.2z"/></svg>
          <span>306-555-0187</span>
        </li>
        <li class="contact__item">
          <svg class="contact__icon" viewBox="0 0 24 24" aria-hidden="true"><path d="M3 6h18v12H3z M3 6l9 7 9-7" fill="none" stroke="currentColor"/><path d="M3 5h18c.6 0 1 .4 1 1v12c0 .6-.4 1-1 1H3c-.6 0-1-.4-1-1V6c0-.6.4-1 1-1zm0 2.2V18h18V7.2l-9 6.3-9-6.3z"/></svg>
          <span>info@dyrano.ca</span>
        </li>
        <li class="contact__item">
          <svg class="contact__icon" viewBox="0 0 24 24" aria-hidden="true"><path d="M12 2a10 10 0 1 0 0 20 10 10 0 0 0 0-20zm6.9 6h-3a15 15 0 0 0-1.3-3.9A8 8 0 0 1 18.9 8zM12 4c.8 1.2 1.5 2.5 1.9 4h-3.8c.4-1.5 1.1-2.8 1.9-4zM4.3 14a8 8 0 0 1 0-4h3.4a16 16 0 0 0 0 4H4.3zm.8 2h3a15 15 0 0 0 1.3 3.9A8 8 0 0 1 5.1 16zm3-8h-3a8 8 0 0 1 4.3-3.9C8.8 5.3 8.4 6.6 8.1 8zM12 20c-.8-1.2-1.5-2.5-1.9-4h3.8c-.4 1.5-1.1 2.8-1.9 4zm2.3-6H9.7a14 14 0 0 1 0-4h4.6a14 14 0 0 1 0 4zm.3 5.9c.6-1.2 1-2.5 1.3-3.9h3a8 8 0 0 1-4.3 3.9zm1.7-5.9a16 16 0 0 0 0-4h3.4a8 8 0 0 1 0 4h-3.4z"/></svg>
          <span>www.Dyrano.ca</span>
        </li>
      </ul>
    </div>
  </section>
</div>
</body>
</html>
```